Banner Ad Design Project

We need a 728x90 and a 300x250
1st option
"I have a lead for you. Click here to close the deal."
In large bold letters.
Under this in smaller letters,
"Borwelt. For serious business networkers"
2nd option
"Put that coffee down!"
"Coffee's for closers only."
Close more deals. BORWELT LOGO
(this is a quote from Harrowmere Tavish. It is a famous sales movie)
The other option is
"First you get the money" "Then you get the power" in bold letters.
"Borwelt. For serious business networkers" in smaller letters at the bottom.
-Must have our colors
-Must have our logo (Small at the bottom right)
-Watch the video at borwelt () com
Please be creative. If the banner can have multiple images that would be great as well.
This needs to be a serious looking ad that is bold and clean.
Updates
Please be sure to use the phrase, "Put that coffee down! Coffee's for closers only" with the logo and at the bottom the words, Borwelt, for serious business networkers. in one of the designs. This will be our first campaign. I am looking for a very simple design that is bold. Perhaps just a coffee cup with the words and no other graphics.
Target Market(s)
Sales professionals
Industry/Entity Type
Business
Look and feel

```html
<!DOCTYPE html>
<html lang="en">
<head>
<meta charset="utf-8">
<title>Borwelt banner set</title>
<link href="https://fonts.googleapis.com/css2?family=Ubuntu:wght@500;700&family=Arimo:wght@400;700&display=swap" rel="stylesheet">
<style>
  :root {
    --stage: #6b4526;
    --paper: #ffffff;
    --orange: #f4a11b;
    --navy: #2e4c9a;
    --green: #7ab648;
    --button-top: #ffe34d;
    --button-bottom: #f2b800;
    --button-edge: #c99400;
  }
  * { box-sizing: border-box; margin: 0; padding: 0; }
  html, body { width: 1200px; height: 804px; overflow: hidden; }
  body { background: var(--stage); position: relative; font-family: "Ubuntu", sans-serif; }

  .banner {
    position: absolute;
    background: var(--paper);
    border-top: 4px solid var(--green);
    box-shadow: 3px 4px 8px rgba(0,0,0,.45);
    display: flex; flex-direction: column; align-items: center; justify-content: center;
    text-align: center;
  }
  .banner::after {
    content: ""; position: absolute; left: 0; right: 0; bottom: 0; height: 7px;
    border-top: 2px solid var(--navy); border-bottom: 3px solid var(--navy);
    background: #dfe4f1;
  }
  .rect { top: 109px; width: 318px; height: 262px; padding-bottom: 8px; }
  .rect-close { left: 85px; }
  .rect-money { left: 440px; }
  .rect-lead { left: 798px; }
  .leader { left: 213px; width: 773px; height: 94px; padding-bottom: 8px; }
  .leader-lead { top: 404px; }
  .leader-money { top: 532px; }
  .leader-close { top: 659px; flex-direction: row; gap: 26px; }

  .headline { color: var(--orange); font-weight: 700; line-height: 1.2; }
  .tagline { font-family: "Arimo", sans-serif; color: var(--navy); font-size: 16px; }

  .cta {
    display: inline-block; font-family: "Arimo", sans-serif; font-weight: 700; font-size: 13px;
    color: #222; padding: 4px 22px; border: 1px solid var(--button-edge);
    background: linear-gradient(var(--button-top), var(--button-bottom));
  }

  .brand { display: flex; align-items: center; gap: 8px; color: var(--navy); font-weight: 500; }
  .brand-mark { background: var(--green); border-radius: 4px; }
  .brand-lg { font-size: 36px; }
  .brand-lg .brand-mark { width: 40px; height: 40px; }
  .brand-md { font-size: 26px; }
  .brand-md .brand-mark { width: 30px; height: 30px; }
  .brand-sm { position: absolute; right: 8px; bottom: 13px; font-size: 9px; gap: 3px; }
  .brand-sm .brand-mark { width: 12px; height: 12px; border-radius: 2px; }
  .brand-stack { flex-direction: column; gap: 2px; font-size: 14px; }
  .brand-stack .brand-mark { width: 44px; height: 44px; border-radius: 5px; }
</style>
</head>
<body>

  <section class="banner rect rect-close">
    <p class="headline" style="font-size:66px;line-height:1">Close</p>
    <p class="headline" style="font-size:48px;line-height:1.2;margin-bottom:14px">more deals</p>
    <div class="brand brand-lg"><span class="brand-mark"></span>Borwelt</div>
  </section>

  <section class="banner rect rect-money">
    <p class="headline" style="font-size:32px;line-height:1.3">First you get the<br>money.<br>Then you get the<br>power.</p>
    <div class="brand brand-md" style="margin:6px 0 6px"><span class="brand-mark"></span>Borwelt</div>
    <p class="tagline">For serious business networkers.</p>
  </section>

  <section class="banner rect rect-lead">
    <p class="headline" style="font-size:27px">I have a lead for you.</p>
    <span class="cta" style="margin:10px 0 8px;padding:4px 24px">Click Here</span>
    <p class="headline" style="font-size:27px">To close the deal.</p>
    <div class="brand brand-md" style="margin:16px 0 14px"><span class="brand-mark"></span>Borwelt</div>
    <p class="tagline">For serious business networkers.</p>
  </section>

  <section class="banner leader leader-lead">
    <div style="display:flex;align-items:center;gap:24px">
      <p class="headline" style="font-size:28px">I have a lead for you.</p>
      <span class="cta">Click Here</span>
      <p class="headline" style="font-size:28px">To close the deal.</p>
    </div>
    <p class="tagline" style="margin-top:4px">Borwelt. For serious business networkers.</p>
    <div class="brand brand-sm"><span class="brand-mark"></span>Borwelt</div>
  </section>

  <section class="banner leader leader-money">
    <p class="headline" style="font-size:31px">First you get the money. Then you get the power.</p>
    <p class="tagline" style="margin-top:4px">Borwelt. For serious business networkers.</p>
    <div class="brand brand-sm"><span class="brand-mark"></span>Borwelt</div>
  </section>

  <section class="banner leader leader-close">
    <p class="headline" style="font-size:60px">Close more deals.</p>
    <div class="brand brand-stack"><span class="brand-mark"></span>Borwelt</div>
  </section>

</body>
</html>
```